Business Card Design for Mabel's Pantry

We make food for dogs.
Business Card Design (using the logo designed by you). Our Brand color is a bright canary yellow. For example our signage is predominantly yellow, with the logo in black. I'd like the card also to use that imagery.
Feel free to use the two sides creatively.
Vertical Design is also great.

Industry/Entity Type

Pet food

Contact Information for Business Card

Name, email, website, phone no

Font styles to use
Sans Serif

Colors
59FF00
82FF00
B8FF75
E3FFCB
F4FFEA
FFF300
FFF600
FEFA6F
FFFEC7
FFFEE8

Requirements
Nice to have
• A graphic in the same brush stroke style of the logo shoeing a doggy bowl of food

```html
<!DOCTYPE html>
<html lang="en">
<head>
<meta charset="utf-8">
<title>Mabel's Pantry – Business Card</title>
<link rel="stylesheet" href="https://fonts.googleapis.com/css2?family=Barlow+Condensed:wght@400;500;600&display=swap">
<style>
  :root {
    --canvas-bg: #c9cacc;
    --canary: #ffe150;
    --canary-deep: #f2cf3a;
    --ink: #151515;
    --paper: #ffffff;
    --accent: #ffe54f;
  }
  * { margin: 0; padding: 0; box-sizing: border-box; }
  html, body { width: 1200px; height: 900px; overflow: hidden; }
  body {
    position: relative;
    background: var(--canvas-bg);
    font-family: "Barlow Condensed", "Arial Narrow", sans-serif;
  }
  .card {
    position: absolute;
    top: 116px;
    width: 383px;
    height: 670px;
    border-radius: 12px;
    overflow: hidden;
  }
  .card--front { left: 182px; background: var(--canary); }
  .card--back { left: 638px; background: var(--ink); color: var(--paper); }

  .line {
    position: absolute;
    left: 0;
    width: 100%;
    text-align: center;
    white-space: nowrap;
  }
  .front-brand {
    top: 358px;
    font-size: 58px;
    font-weight: 400;
    letter-spacing: 0.5px;
    color: var(--canary-deep);
    line-height: 64px;
  }
  .brand-mark {
    position: absolute;
    left: 161px;
    top: 66px;
    width: 60px;
    height: 60px;
    border-radius: 50%;
    background: var(--accent);
  }
  .back-brand {
    top: 138px;
    font-size: 46px;
    font-weight: 400;
    color: var(--accent);
    line-height: 52px;
  }
  .person-name {
    top: 294px;
    font-size: 31px;
    font-weight: 600;
    letter-spacing: 1.5px;
    color: var(--accent);
    line-height: 36px;
  }
  .person-role {
    top: 333px;
    font-size: 18px;
    font-weight: 500;
    letter-spacing: 1.5px;
    line-height: 22px;
  }
  .contact-icons {
    position: absolute;
    top: 365px;
    left: 0;
    width: 100%;
    display: flex;
    justify-content: center;
    gap: 7px;
  }
  .contact-icons svg { width: 13px; height: 13px; fill: var(--accent); }
  .contact {
    font-size: 17px;
    font-weight: 500;
    letter-spacing: 1.5px;
    line-height: 20px;
  }
  .contact--phone { top: 390px; }
  .contact--email { top: 413px; }
  .contact--web { top: 437px; }
  .pin {
    position: absolute;
    left: 184px;
    top: 474px;
    width: 15px;
    height: 21px;
    fill: var(--accent);
  }
  .address { font-size: 17px; font-weight: 500; letter-spacing: 0.8px; line-height: 20px; }
  .address--1 { top: 505px; }
  .address--2 { top: 526px; }
  .address--3 { top: 548px; }
  .social {
    top: 596px;
    font-size: 19px;
    font-weight: 500;
    letter-spacing: 0.8px;
    line-height: 24px;
  }
</style>
</head>
<body>
  <section class="card card--front" aria-label="Card front">
    <p class="line front-brand">MABEL'S PANTRY</p>
  </section>

  <section class="card card--back" aria-label="Card back">
    <div class="brand-mark" aria-hidden="true"></div>
    <p class="line back-brand">MABEL'S PANTRY</p>

    <p class="line person-name">TRAVIS MABEL</p>
    <p class="line person-role">Owner</p>

    <div class="contact-icons" aria-hidden="true">
      <svg viewBox="0 0 16 16"><path d="M3.5 1l2.6 3-1.4 1.8c.9 2 2.5 3.6 4.5 4.5l1.8-1.4 3 2.6-1.3 2.4C7.2 14 2 8.8 1.1 3z"/></svg>
      <svg viewBox="0 0 16 16"><path d="M1 3h14v1.2L8 8.6 1 4.2z"/><path d="M1 5.8l7 4.4 7-4.4V13H1z"/></svg>
      <svg viewBox="0 0 16 16"><circle cx="8" cy="8" r="7"/><path d="M5 4.5c1.5 0 2.3 1 2 2.2-.4 1.3-2 1-2.2 2.5-.2 1.2 1 2.5.5 4" stroke="#151515" stroke-width="1.3" fill="none"/><path d="M10.5 3.5c-.6 1.5.8 2.3 2 2.6" stroke="#151515" stroke-width="1.3" fill="none"/></svg>
    </div>
    <p class="line contact contact--phone">555-014-2290</p>
    <p class="line contact contact--email">travis@mabelspantry.com</p>
    <p class="line contact contact--web">www.MabelsPantry.com</p>

    <svg class="pin" viewBox="0 0 15 21" aria-hidden="true"><path d="M7.5 0A7.5 7.5 0 0 0 0 7.5C0 13 7.5 21 7.5 21S15 13 15 7.5A7.5 7.5 0 0 0 7.5 0zm0 10.3a2.8 2.8 0 1 1 0-5.6 2.8 2.8 0 0 1 0 5.6z"/></svg>
    <p class="line address address--1">418 E. Harlow Ave</p>
    <p class="line address address--2">P.O. Box 217</p>
    <p class="line address address--3">Linden Bay, FL 30412</p>

    <p class="line social">mabel'spantry</p>
  </section>
</body>
</html>
```